Bed & Breakfast Wordpress Theme - Design Only

We are looking for a Wordpress theme for an award winning UK Bed & Breakfast (Guesthouse) www.fernbrookinn.co.uk
You will see that the current site is basic and dated, we need a new site that showcases the very high standard of rooms on offer and is geared towards both mobile and desktop browsing.
We would like the colours that have been used in the rooms and building (as seen on the current website) to feature in the design.
We particularly like the look of this accommodation provider website: http://www.marlowdenbarns.co.uk
Selected website images can be downloaded here, feel free to use more from the existing website too:
https://www.filevaultly.com/s/qz81mv4rt7kw0pn/website%20images.zip
Target Market(s)
The accommodation is upmarket and the design needs to subtly communicate this.
The accommodation attracts a varied mix of ages so needs to be up scale without being overly modern.
Industry/Entity Type
Accommodation
Requirements
Must have
- As the accommodation does not have a logo we need a basic typographic logo incorporated into the design.
Colours of the building and rooms must be integrated into the design in some way.
A bold homepage that allows images of the rooms on offer and key information to be visibale above the fold. The goal of the homepage is for someone to then click Rooms or Prices so calls to action may help here.
Separate designs for a sidebar and full width version of sub pages.
An area that shows off the awards won by the company on all pages and space for testimonials.
The site must enable an easy transition from - homepage - to rooms - to prices with possible call to action buttons in the top right corner on these pages
The site needs to have a Homepage layout, a general sub page layout, and a 'Rooms' page layout which will showcase all rooms available possibly in a grid layout.
Nice to have
- Please use some of the images available currently on the website in your mockup, particularly of the building and rooms.
Should not have
- No need for any type of booking fields or engine as the booking system will be embedded on a full width page.

```html
<!DOCTYPE html>
<html lang="en">
<head>
<meta charset="utf-8">
<title>Fernbrook Inn – A Small and Friendly Hotel</title>
<link href="https://fonts.googleapis.com/css2?family=Lato:wght@400;700&family=Great+Vibes&display=swap" rel="stylesheet">
<style>
:root{
  --green:#5a9a1f;
  --green-dark:#3f7c12;
  --green-light:#7cb83a;
  --green-pale:#9fd07a;
  --text:#555;
  --heading:#222;
  --rule:#dcdcdc;
  --footer:#2c2c2c;
  --footer-deep:#1f1f1f;
  --panel:#e7e7e7;
}
*{box-sizing:border-box;margin:0;padding:0}
html,body{width:1200px;height:2161px;overflow:hidden}
body{position:relative;background:#fff;font-family:Lato,Arial,sans-serif;color:var(--text)}
.abs{position:absolute}
/* hero */
.hero{left:0;top:0;width:1200px;height:386px;background:linear-gradient(100deg,#6e5a2c 0%,#b59a5a 22%,#4a3a22 45%,#6b5a3e 60%,#2b2219 80%,#4a3b26 100%)}
.hero-shade{left:0;top:0;width:1200px;height:386px;background:linear-gradient(180deg,rgba(0,0,0,.45),rgba(0,0,0,0) 30%,rgba(0,0,0,.1))}
.contact-top{top:12px;font-size:12px;color:var(--green-light);text-align:center}
.contact-top svg{display:block;margin:0 auto 2px}
.contact-top.phone{left:240px}
.contact-top.mail{left:800px;color:#fff}
.contact-top.mail b{font-weight:400;color:var(--green-light)}
.brand{left:500px;top:62px;width:200px;text-align:center;font-size:24px;color:#fff;font-weight:400;letter-spacing:1px}
.brand i{display:block;width:14px;height:14px;border:2px solid #fff;border-radius:50%;margin:0 auto 8px}
.tagline{left:0;top:176px;width:1200px;text-align:center;font-family:'Great Vibes',cursive;font-size:62px;color:#fff;text-shadow:0 2px 6px rgba(0,0,0,.5)}
/* band */
.band{left:0;top:386px;width:1200px;height:272px;background:linear-gradient(90deg,#cbbd9e 0%,#efe7d6 30%,#f4ede0 55%,#e8ddc6 80%,#d8c8a5 100%)}
.band-deer{left:80px;top:430px;width:140px;height:170px;background:radial-gradient(ellipse at center,rgba(110,95,75,.45),rgba(110,95,75,0) 70%)}
.nav{left:249px;top:360px;width:702px;height:51px;background:linear-gradient(180deg,var(--green-light),var(--green-dark));display:flex;justify-content:space-around;align-items:center;padding:0 40px;box-shadow:0 2px 4px rgba(0,0,0,.3)}
.nav a{color:#fff;text-decoration:none;font-size:14px}
.nav a.current{text-decoration:underline}
.slider{left:253px;top:429px;width:463px;height:202px;background:linear-gradient(110deg,#1f2a45 0%,#5a4630 35%,#3a2c20 55%,#8a7150 80%,#4b3a28 100%);border:3px solid #fff;box-shadow:0 1px 4px rgba(0,0,0,.3)}
.slider-caption{left:0;bottom:0;width:100%;height:54px;background:rgba(255,255,255,.35);padding:6px 8px;font-size:11px;color:#fff}
.btn{display:inline-block;background:var(--green);color:#fff;font-size:10px;padding:3px 8px;margin-top:10px}
.slider-arrows{right:8px;bottom:8px;display:flex;gap:2px}
.slider-arrows span{width:15px;height:15px;background:var(--green);color:#fff;font-size:11px;line-height:15px;text-align:center}
.sidemenu{left:733px;top:428px;width:215px;list-style:none}
.sidemenu li{height:19px;margin-bottom:1.7px;background:linear-gradient(180deg,#fff,#e4e4e4);font-size:10px;color:#333;line-height:19px;padding:0 10px;display:flex;justify-content:space-between}
.sidemenu li.active{background:var(--green);color:#fff}
/* main */
.main{left:249px;top:658px;width:702px;height:1173px;background:#fff}
h1.welcome,h2.section{color:var(--green);font-size:18px;font-weight:700}
h2.plain{color:var(--heading);font-size:17px;font-weight:400}
.copy{font-family:Arial,sans-serif;font-size:8.6px;line-height:16px;color:#555;width:530px}
.rule{height:1px;background:var(--rule)}
.filters{font-size:9.5px;color:#999;line-height:15px;width:600px}
.filters b{color:var(--green);font-weight:400}
.tile{width:206px;height:111px;border:1px solid #ccc}
.dots{display:flex;gap:6px;align-items:center}
.dots i{width:12px;height:12px;border-radius:50%;background:var(--green)}
.dots i.on{background:#fff;border:3px solid var(--green)}
.arrow{color:var(--green);font-size:14px}
.video{left:268px;top:1301px;width:206px;height:158px;background:linear-gradient(120deg,#3a2a18,#9a7a48 50%,#2a2014)}
.video-bar{left:0;bottom:0;width:100%;height:14px;background:#111;font-size:6px;color:#aaa;padding:3px}
.chef{left:497px;top:1301px;width:206px;height:158px;background:linear-gradient(135deg,#f3f3f3,#d9d4cc 60%,#b8a890);border:1px solid #ddd}
.chef-cap{left:0;bottom:0;width:100%;height:38px;background:var(--green);color:#fff;font-size:9px;text-align:center;padding-top:5px;line-height:12px}
.widget{left:726px;top:1301px;width:205px;height:346px;background:var(--panel);padding:10px 13px;font-size:8.5px;color:#333;line-height:14px}
.widget .w-brand{font-size:15px;font-weight:700;color:#222;display:flex;align-items:center;gap:5px}
.widget .w-brand i{width:11px;height:11px;border-radius:50%;background:#222;display:inline-block}
.widget hr{border:0;border-top:1px solid #777;margin:6px 0}
.widget h4{font-size:12px;color:#111}
.widget u{color:#555}
.rating{display:flex;gap:2px;margin:3px 0}
.rating i{width:8px;height:8px;border-radius:50%;background:var(--green)}
.big6{font-size:16px;color:var(--green);font-weight:700}
.cert{left:268px;top:1487px;width:206px;height:160px;background:#f1ede4;border:1px solid #ccc;text-align:center;font-size:13px;color:#444}
.cert .yr{color:var(--green)}
.cert .low{left:0;bottom:0;width:100%;height:60px;background:var(--green);color:#fff;padding-top:28px}
.cert .seal{left:78px;top:50px;width:50px;height:50px;border-radius:50%;background:#fff;border:4px solid var(--green)}
.recommend{left:497px;top:1487px;width:206px;height:160px;background:radial-gradient(circle,#b3dc93,#8cc463);color:#fff;text-align:center;padding-top:58px;font-size:16px;font-weight:700;letter-spacing:.5px}
.recommend .r-brand{color:#222;font-size:20px;display:flex;justify-content:center;align-items:center;gap:6px;margin-top:4px}
.recommend .r-brand i{width:16px;height:16px;border-radius:50%;background:#222;display:inline-block}
.awards-title{left:249px;top:1690px;width:702px;text-align:center;font-size:17px;color:#222;font-weight:700}
.awards{left:268px;top:1738px;width:663px;height:60px;display:flex;align-items:center;justify-content:space-between}
.awards .sep{width:1px;height:30px;background:#ccc}
.badge{background:#d5d9de}
.contact-bar{left:249px;top:1831px;width:702px;height:49px;background:var(--green);color:#fff;font-size:11px;padding:6px 18px;line-height:18px}
.contact-bar svg{vertical-align:-2px;margin-right:6px}
.social{right:16px;top:10px;display:flex;gap:5px}
.social i{width:26px;height:26px;border-radius:50%;background:#fff}
/* footer */
.footer{left:0;top:1916px;width:1200px;height:245px;background:var(--footer)}
.footer-bottom{left:0;top:2133px;width:1200px;height:28px;background:var(--footer-deep)}
.newsletter{left:249px;top:1949px;width:291px;height:184px;background:var(--green);text-align:center;color:#fff;padding:16px 16px}
.newsletter h3{font-size:20px;font-weight:700}
.newsletter p{font-size:9px;line-height:13px;margin:12px 20px 8px}
.field{display:block;width:260px;height:27px;background:#fff;color:#666;font-size:10px;text-align:left;padding:8px 10px;margin:0 auto 6px}
.subscribe{display:block;width:70px;background:#2a2a2a;color:#fff;font-size:9px;padding:4px;margin-left:0}
.fcol{top:1948px;font-size:8.5px;color:#ddd;line-height:14.5px}
.fcol h4{color:var(--green-light);font-size:12px;line-height:14px;margin-bottom:14px;font-weight:700}
.fcol ul{list-style:none}
.fcol p{width:150px;line-height:14.5px}
.fcol .client{color:var(--green-light);margin-top:12px}
.copyright{left:573px;top:2142px;font-size:8px;color:#ccc}
.social-sm{left:871px;top:2139px;display:flex;gap:3px}
.social-sm i{width:15px;height:15px;border-radius:50%;background:#888}
</style>
</head>
<body>

<header>
  <div class="abs hero" role="img" aria-label="Photo of a warmly lit hotel bedroom with a made bed and seating"></div>
  <div class="abs hero-shade"></div>
  <div class="abs contact-top phone">
    <svg width="14" height="12" viewBox="0 0 14 12"><path d="M2 4c0-2 3-3 5-3s5 1 5 3l-2 1-1-1H5L4 5z M4 6h6l2 5H2z" fill="#7cb83a"/></svg>
    01632 960418
  </div>
  <div class="abs contact-top mail">
    <svg width="14" height="10" viewBox="0 0 14 10"><rect x="0" y="0" width="14" height="10" fill="#7cb83a"/><path d="M0 0l7 6 7-6" stroke="#fff" fill="none"/></svg>
    enquiries@<b>fernbrookinn.co.uk</b>
  </div>
  <div class="abs brand"><i></i>Fernbrook Inn</div>
  <div class="abs tagline">A Small and friendly Hotel.</div>
</header>

<div class="abs band" role="img" aria-label="Soft pale photo of a misty forest meadow"></div>
<div class="abs band-deer" role="img" aria-label="Faint stag standing in the meadow"></div>

<nav class="abs nav">
  <a class="current" href="#">Home</a><a href="#">Rooms</a><a href="#">Prices</a><a href="#">Picture Gallery</a><a href="#">Information</a><a href="#">Sitemap</a>
</nav>

<section class="abs slider" role="img" aria-label="Slideshow photo of a guest room overlooking a city at night">
  <div class="abs slider-caption">Lorem Ipsum is simply dummy text of the printing and typesetting industry.<br><span class="btn">Book Online</span></div>
  <div class="abs slider-arrows"><span>‹</span><span>›</span></div>
</section>

<ul class="abs sidemenu">
  <li>Book Online<span>›</span></li><li>Rooms<span>›</span></li><li>Special Offers<span>›</span></li><li>Gift Vouchers<span>›</span></li><li class="active">Awards<span>›</span></li><li>New Forest Video<span>›</span></li><li>B&amp;B Accessibility<span>›</span></li><li>Welcome Video<span>›</span></li><li>Our Environment<span>›</span></li><li>Leave the car at home<span>›</span></li>
</ul>

<main class="abs main"></main>

<h1 class="abs welcome" style="left:265px;top:675px">Welcome to Fernbrook Inn.</h1>
<p class="abs copy" style="left:265px;top:705px">Lorem Ipsum is simply dummy text of the printing and typesetting industry. Lorem Ipsum has been the industry's standard dummy text ever since the 1500s, when an unknown printer took a galley of type and scrambled it to make a type specimen book. It has survived not only five centuries, but also the leap into electronic typesetting, remaining essentially unchanged. It was popularised in the 1960s with the release of TypeSheet sheets containing Lorem Ipsum passages, and more recently with desktop publishing software like PageSetter Pro including versions of Lorem Ipsum.</p>
<h2 class="abs plain" style="left:263px;top:800px">Christmas and New Year</h2>
<p class="abs copy" style="left:265px;top:827px">Lorem Ipsum has been the industry's standard dummy text ever since the 1500s, when an unknown printer took a galley of type and scrambled it to make a type specimen book.</p>
<div class="abs rule" style="left:265px;top:877px;width:667px"></div>

<h2 class="abs section" style="left:265px;top:893px">Gallery</h2>
<p class="abs filters" style="left:268px;top:925px"><b>All</b> / Book Online / Rooms / Special Offers / Gift Vouchers / New Forest Video / B&amp;B Accessibility / Welcome Video<br>Our Environment / Leave the car at home</p>

<div class="abs tile" style="left:268px;top:970px;background:linear-gradient(120deg,#c9a060,#7a5530 60%,#3a2a20)" role="img" aria-label="Glasses of juice on a bedside"></div>
<div class="abs tile" style="left:497px;top:970px;background:linear-gradient(180deg,#8aa8c0,#5f7a40 50%,#8a9a60)" role="img" aria-label="Wedding couple by a garden pond in front of the inn"></div>
<div class="abs tile" style="left:726px;top:970px;background:linear-gradient(120deg,#2a1a18,#7a3a5a 50%,#3a2430)" role="img" aria-label="Bedroom with purple lighting"></div>
<div class="abs tile" style="left:268px;top:1103px;background:radial-gradient(circle at 40% 40%,#f0b040,#b06010 60%,#5a2a08)" role="img" aria-label="Festive golden gift and lights"></div>
<div class="abs tile" style="left:497px;top:1103px;background:linear-gradient(180deg,#e8e6e0,#b0aca4 55%,#3a3430)" role="img" aria-label="Modern room with dark floor"></div>
<div class="abs tile" style="left:726px;top:1103px;background:linear-gradient(180deg,#cfc8bc,#8a7e70 60%,#5a5048)" role="img" aria-label="Double bedroom with grey headboard"></div>

<div class="abs dots" style="left:508px;top:1234px"><span class="arrow">‹</span><span style="width:30px"></span><i class="on"></i><i></i><i></i><i></i><i></i><span style="width:30px"></span><span class="arrow">›</span></div>
<div class="abs rule" style="left:265px;top:1275px;width:667px"></div>

<div class="abs video" role="img" aria-label="Video still of a hotel bedroom">
  <svg class="abs" style="left:88px;top:62px" width="30" height="22" viewBox="0 0 30 22"><rect width="30" height="22" rx="5" fill="#222" opacity=".8"/><path d="M12 6l8 5-8 5z" fill="#fff"/></svg>
  <div class="abs video-bar">0:42 / 3:20</div>
</div>
<div class="abs chef" role="img" aria-label="Chef plating a dish">
  <div class="abs chef-cap">Why not book dinner at<br><b>www.oakhollowkitchen.co.uk</b><br>at the Fernbrook Inn</div>
</div>

<aside class="abs widget">
  <div class="w-brand"><i></i>StayRater</div>
  <div style="color:#666;margin-top:4px">Offering 479 reviews of <u>Fernbrook Inn</u> in Ashcombe</div>
  <hr>
  <h4>Fernbrook Inn</h4>
  <b>StayRater Traveller Rating:</b>
  <div class="rating"><i></i><i></i><i></i><i></i><i></i></div>
  <div style="color:#666">Based on 479 traveller reviews</div>
  <hr>
  <div>StayRater Popularity Index:</div>
  <div><span class="big6">#6</span> of 31 B&amp;Bs in Ashcombe</div>
  <hr>
  <b>Most Recent Traveller Reviews:</b>
  <div>17 Dec 2013: "Lovely Stay"<br>9 Dec 2013: "Charming and very relaxing!"<br>2 Dec 2013: "Perfection"<br>2 Dec 2013: "Wonderful B&amp;B"<br>18 Nov 2013: "Excellent"</div>
  <div style="margin-top:12px">Read reviews &nbsp;|&nbsp; Write a review</div>
  <div style="margin-top:12px;color:#666">© 2014 StayRater LLC</div>
</aside>

<div class="abs cert">
  <div style="margin-top:12px">Certificate of Excellence</div>
  <div class="yr">2013 WINNER</div>
  <div class="abs low">Fernbrook Inn</div>
  <div class="abs seal"></div>
</div>
<div class="abs recommend">RECOMMENDED ON<div class="r-brand"><i></i>StayRater</div></div>

<div class="abs rule" style="left:265px;top:1675px;width:667px"></div>
<h2 class="abs awards-title">Awards</h2>
<div class="abs awards">
  <div class="badge" style="width:54px;height:54px;border-radius:50%;background:#243a6a"></div><span class="sep"></span>
  <div class="badge" style="width:150px;height:44px;background:#e9dcc6"></div><span class="sep"></span>
  <div class="badge" style="width:44px;height:54px;border-radius:50%;background:#e8b84a"></div><span class="sep"></span>
  <div class="badge" style="width:105px;height:20px;background:#cfcfcf"></div><span class="sep"></span>
  <div class="badge" style="width:100px;height:40px;background:#c9d3e2"></div><span class="sep"></span>
  <div class="badge" style="width:70px;height:36px;background:#dedede"></div>
</div>

<div class="abs contact-bar">
  <div><svg width="12" height="11" viewBox="0 0 14 12"><path d="M2 4c0-2 3-3 5-3s5 1 5 3l-2 1-1-1H5L4 5z M4 6h6l2 5H2z" fill="#fff"/></svg>01632 960418 &nbsp;&nbsp;&nbsp;<svg width="13" height="9" viewBox="0 0 14 10"><rect width="14" height="10" fill="#fff"/><path d="M0 0l7 6 7-6" stroke="#5a9a1f" fill="none"/></svg>enquiries@fernbrookinn.co.uk</div>
  <div><svg width="12" height="11" viewBox="0 0 12 11"><path d="M6 0l6 5h-2v6H7V7H5v4H2V5H0z" fill="#fff"/></svg>Fernbrook Inn, Mill Lane, Ashcombe, Hampshire SO99 4XT</div>
  <div class="abs social"><i></i><i></i><i></i></div>
</div>

<footer>
  <div class="abs footer"></div>
  <div class="abs footer-bottom"></div>
  <form class="abs newsletter">
    <h3>Newsletters Sign Up</h3>
    <p>Sign up for our daily email by entering your information below</p>
    <span class="field">Your name</span>
    <span class="field">Email address</span>
    <span class="subscribe">Subscribe</span>
  </form>
  <div class="abs fcol" style="left:573px">
    <h4>Quick Links</h4>
    <ul><li>Home</li><li>Rooms</li><li>Prices</li><li>Gallery</li><li>Special Offers</li><li>Gift Vouchers</li><li>Awards</li><li>Information</li><li>Sitemap</li></ul>
  </div>
  <div class="abs fcol" style="left:691px">
    <h4>Support<br>Links</h4>
    <ul style="margin-top:-14px"><li>New Forest Video</li><li>B&amp;B Accessibility</li><li>Welcome Video</li><li>Our Environment</li><li>Leave the car at home</li><li>Privacy Policy</li><li>Term of Use</li><li>Help</li><li>Contact</li></ul>
  </div>
  <div class="abs fcol" style="left:798px">
    <h4>Client's Testimonials</h4>
    <p>Lorem Ipsum is simply dummy text of the printing and typesetting industry. Lorem Ipsum has been the industry's standard dummy text ever since the 1500s, when an unknown printer took a galley of type and scrambled it to make a type specimen book.</p>
    <p class="client">Client name, City</p>
  </div>
  <div class="abs copyright">Copyright © 2014 Fernbrook Inn. &nbsp;&nbsp; All rights reserved.</div>
  <div class="abs social-sm"><i></i><i></i><i></i></div>
</footer>

</body>
</html>
```